VARQO Business card

Black card, double sided with company colors black, blue and white with slogan on back Your VARQO......

Industry/Entity Type

Business

```html
<!DOCTYPE html>
<html lang="en">
<head>
<meta charset="utf-8">
<title>VARQO Business Card</title>
<link rel="stylesheet" href="https://fonts.googleapis.com/css2?family=Jost:wght@400;500&display=swap">
<style>
  :root {
    --page: #8a8a8a;
    --card-black: #050505;
    --card-sheen: #2c2c2c;
    --brand-blue: #3fb8e0;
    --band-light: #5ccfee;
    --band-deep: #35a7d6;
    --white: #ffffff;
    --soft-white: #e6e6e6;
  }
  * { box-sizing: border-box; margin: 0; padding: 0; }
  html, body { width: 1200px; height: 1200px; overflow: hidden; }
  body {
    background: var(--page);
    font-family: "Jost", sans-serif;
    position: relative;
  }
  .card {
    position: absolute;
    left: 275px;
    width: 650px;
    height: 390px;
    border-radius: 24px;
    overflow: hidden;
    background:
      linear-gradient(90deg, transparent 16%, rgba(255,255,255,0.16) 26%, var(--card-sheen) 36%, transparent 52%, rgba(255,255,255,0.06) 68%, transparent 80%),
      var(--card-black);
    box-shadow: 0 6px 14px rgba(0,0,0,0.35);
  }
  .card--front { top: 205px; }
  .card--back { top: 645px; }

  .brand {
    position: absolute;
    display: flex;
    align-items: center;
    color: var(--white);
    font-weight: 400;
    letter-spacing: 0.04em;
  }
  .brand__dot {
    display: inline-block;
    border-radius: 50%;
    background: var(--brand-blue);
  }
  .card--front .brand { left: 45px; top: 38px; font-size: 46px; gap: 12px; }
  .card--front .brand__dot { width: 30px; height: 30px; }
  .card--back .brand { left: 34px; top: 320px; font-size: 32px; gap: 8px; }
  .card--back .brand__dot { width: 22px; height: 22px; }

  .person {
    position: absolute;
    right: 36px;
    top: 46px;
    text-align: right;
  }
  .person__name { color: var(--white); font-size: 29px; font-weight: 400; line-height: 1.05; }
  .person__role { color: var(--brand-blue); font-size: 21px; font-weight: 500; margin-right: 32px; line-height: 1; }

  .contact-band {
    position: absolute;
    left: 0; right: 0;
    top: 181px;
    height: 146px;
    background: linear-gradient(90deg, var(--band-deep), var(--band-light) 40%, var(--band-deep));
    color: var(--white);
    font-size: 18px;
    letter-spacing: 0.02em;
  }
  .contact-list { position: absolute; left: 50px; top: 46px; list-style: none; }
  .contact-list li { display: flex; align-items: center; gap: 4px; line-height: 25px; }
  .address { position: absolute; right: 24px; top: 50px; text-align: right; line-height: 21px; }
  .address__line { display: flex; align-items: center; justify-content: flex-end; gap: 4px; }
  .icon { fill: var(--card-black); flex: none; }

  .website {
    position: absolute;
    left: 0; right: 0;
    bottom: 22px;
    text-align: center;
    color: var(--soft-white);
    font-size: 17px;
    letter-spacing: 0.05em;
  }

  .slogan {
    position: absolute;
    left: 130px;
    top: 172px;
    color: var(--white);
    font-size: 36px;
    font-weight: 400;
  }
  .back-accent { position: absolute; right: 0; top: 0; }
</style>
</head>
<body>

  <section class="card card--front" aria-label="Card front">
    <div class="brand"><span class="brand__dot"></span>VARQO</div>

    <div class="person">
      <p class="person__name">Marlon Treve</p>
      <p class="person__role">FOUNDER/CEO</p>
    </div>

    <div class="contact-band">
      <ul class="contact-list">
        <li>
          <svg class="icon" width="13" height="20" viewBox="0 0 13 20" aria-hidden="true"><path d="M2 0h9a2 2 0 0 1 2 2v16a2 2 0 0 1-2 2H2a2 2 0 0 1-2-2V2a2 2 0 0 1 2-2zm0 3v12h9V3z"/></svg>
          1.800.555.0142
        </li>
        <li>
          <svg class="icon" width="16" height="11" viewBox="0 0 16 11" aria-hidden="true"><path d="M0 0h16v11H0zM1.5 1.5 8 6.5l6.5-5z" fill-rule="evenodd"/></svg>
          hello@varqo.com
        </li>
      </ul>
      <div class="address">
        <p class="address__line">
          <svg class="icon" width="20" height="17" viewBox="0 0 20 17" aria-hidden="true"><path d="M10 0 20 9h-3v8h-5v-5H8v5H3V9H0z"/></svg>
          410-88 Harbour Street
        </p>
        <p class="address__line">Kelston BC V0X 2K4</p>
      </div>
    </div>

    <p class="website">www.varqomedia.com</p>
  </section>

  <section class="card card--back" aria-label="Card back">
    <svg class="back-accent" width="240" height="390" viewBox="0 0 240 390" aria-hidden="true">
      <circle cx="250" cy="200" r="200" fill="var(--brand-blue)"/>
    </svg>
    <p class="slogan">Your VARQO......</p>
    <div class="brand"><span class="brand__dot"></span>VARQO</div>
  </section>

</body>
</html>
```